Civil engineering company | Billboard

We need a billboard design for Velmora- civil engineering company. We want big logo in the center of billboard and web site (www.velmora.hr) below the logo. Also, we want an subtle abstract pattern in the background. Dimensions of the billboard are: width :10 m, height: 2m. Design must be celan and modern.
Industry/Entity Type
Civil engineering
Font styles to use
Sans Serif
Colors
F0912C
F2A743
F7CA91
FBE8D2
FDF5EE
Requirements
Must have
- Logo and new unique pattern design for Velmroa company
Should not have
- pictures of construction machinery and tools

```html
<!DOCTYPE html>
<html lang="en">
<head>
<meta charset="utf-8">
<title>Velmora – Billboard</title>
<link rel="stylesheet" href="https://fonts.googleapis.com/css2?family=Montserrat:wght@500;600&display=swap">
<style>
  :root {
    --page-bg: #eeeeee;
    --board-white: #ffffff;
    --pattern-light: #FDF5EE;
    --pattern-warm: #FBE8D2;
    --brand-orange: #D99140;
    --brand-orange-light: #E3A45C;
    --band-orange: #D88F3F;
    --band-orange-deep: #D58A38;
    --mark-grey: #8f8f8f;
    --url-white: #ffffff;
  }
  html, body {
    margin: 0;
    padding: 0;
    width: 1200px;
    height: 800px;
    overflow: hidden;
    background: var(--page-bg);
  }
  .canvas {
    position: relative;
    width: 1200px;
    height: 800px;
  }
  .billboard {
    position: absolute;
    left: 40px;
    top: 288px;
    width: 1120px;
    height: 224px;
    background: var(--board-white);
    overflow: hidden;
    box-shadow: 0 2px 10px rgba(0,0,0,0.12);
  }
  .background-pattern {
    position: absolute;
    left: 0;
    right: 0;
    top: 0;
    height: 120px;
    background: linear-gradient(90deg, var(--pattern-light) 0%, var(--board-white) 30%, var(--board-white) 70%, var(--pattern-light) 100%);
  }
  .web-band {
    position: absolute;
    left: 0;
    right: 0;
    top: 120px;
    bottom: 0;
    background: linear-gradient(90deg, var(--brand-orange-light) 0%, var(--band-orange) 25%, var(--band-orange-deep) 100%);
  }
  .brand-square {
    position: absolute;
    left: 180px;
    top: 26px;
    width: 100px;
    height: 136px;
    box-sizing: border-box;
    border: 4px solid var(--mark-grey);
    background: var(--board-white);
  }
  .brand-name {
    position: absolute;
    left: 302px;
    top: 11px;
    margin: 0;
    font-family: "Montserrat", sans-serif;
    font-weight: 500;
    font-size: 122px;
    line-height: 1;
    letter-spacing: 0.03em;
    color: var(--brand-orange);
    text-transform: uppercase;
    white-space: nowrap;
  }
  .web-address {
    position: absolute;
    left: 312px;
    top: 148px;
    margin: 0;
    font-family: "Montserrat", sans-serif;
    font-weight: 600;
    font-size: 44px;
    line-height: 1;
    letter-spacing: 0.42em;
    color: var(--url-white);
    white-space: nowrap;
  }
</style>
</head>
<body>
  <main class="canvas">
    <section class="billboard">
      <div class="background-pattern" role="img" aria-label="Subtle abstract warm-toned geometric background pattern"></div>
      <div class="web-band"></div>
      <div class="brand-square"></div>
      <h1 class="brand-name">Velmora</h1>
      <p class="web-address">www.velmora.hr</p>
    </section>
  </main>
</body>
</html>
```